Brindle Search Business Card for recruitment company

We are looking for a Business Card Design that incorporates our personal details and our busines name and logo. We are a specialized search consultancy that recruit Property and Construction professionals.
We would like a business card that stands out and is appealing to the Construction and Property industry as well.

Target Market(s)

people in the construction and property industry

Contact Information for Business Card

Business Name and logo

Font styles to use
Serif

Colors
0094D4
00A9DD
6FCCEA
C7EBF8
E9F6FB

Requirements
Must have
• Business name and logo as well as contact details
Should not have
• No photos of us please

```html
<!DOCTYPE html>
<html lang="en">
<head>
<meta charset="utf-8">
<title>Brindle Search – Business Card</title>
<link rel="stylesheet" href="https://fonts.googleapis.com/css2?family=Lora:wght@400;600;700&display=swap">
<style>
  :root {
    --stage: #1e2830;
    --brand-blue: #0094d4;
    --bright-blue: #00a9dd;
    --sky-blue: #6fccea;
    --pale-blue: #c7ebf8;
    --mist-blue: #e9f6fb;
    --text-white: #ffffff;
  }
  * { box-sizing: border-box; margin: 0; padding: 0; }
  html, body { width: 1200px; height: 780px; overflow: hidden; }
  body {
    background: var(--stage);
    font-family: "Lora", Georgia, serif;
    display: flex;
    align-items: center;
    justify-content: center;
    gap: 44px;
  }
  .card {
    position: relative;
    width: 540px;
    height: 310px;
    border-radius: 22px;
    background: var(--brand-blue);
    overflow: hidden;
    color: var(--text-white);
  }

  /* Front */
  .brand-mark {
    position: absolute;
    top: 44px;
    left: 0;
    right: 0;
    display: flex;
    align-items: center;
    justify-content: center;
    gap: 12px;
    color: var(--mist-blue);
    font-weight: 700;
    font-size: 30px;
    letter-spacing: 0.5px;
  }
  .brand-dot {
    width: 18px; height: 18px;
    border-radius: 50%;
    background: var(--sky-blue);
    flex: none;
  }
  .details {
    position: absolute;
    left: 30px;
    right: 24px;
    top: 136px;
    display: flex;
    align-items: center;
  }
  .identity { width: 210px; text-align: right; padding-right: 18px; }
  .person-name { font-weight: 700; font-size: 22px; letter-spacing: 0.5px; white-space: nowrap; }
  .person-role { color: var(--pale-blue); font-size: 12px; letter-spacing: 1.5px; margin-top: 2px; white-space: nowrap; }
  .divider { width: 1.5px; height: 80px; background: var(--sky-blue); flex: none; }
  .contacts { list-style: none; padding-left: 18px; font-size: 13px; letter-spacing: 0.5px; line-height: 1.4; }
  .contacts li { display: flex; align-items: flex-start; gap: 8px; margin-bottom: 2px; white-space: nowrap; }
  .contacts svg { flex: none; width: 14px; height: 14px; margin-top: 3px; }
  .web-band {
    position: absolute;
    left: 0; right: 0; bottom: 26px;
    height: 36px;
    background: var(--mist-blue);
    color: var(--brand-blue);
    display: flex;
    align-items: center;
    padding-left: 96px;
    gap: 10px;
    font-size: 17px;
    font-weight: 600;
    letter-spacing: 1px;
  }
  .web-band svg { width: 18px; height: 18px; flex: none; }

  /* Back */
  .card-back { background: var(--brand-blue); }
  .pattern-field {
    position: absolute;
    inset: 0;
    background: linear-gradient(135deg, var(--bright-blue), var(--brand-blue) 70%);
  }
  .back-mark {
    position: absolute;
    right: 70px;
    bottom: 70px;
    display: flex;
    align-items: center;
    gap: 8px;
    color: var(--mist-blue);
    font-weight: 700;
    font-size: 16px;
  }
  .back-mark .brand-dot { width: 10px; height: 10px; }
</style>
</head>
<body>
  <section class="card card-front">
    <div class="brand-mark"><span class="brand-dot"></span>Brindle Search</div>
    <div class="details">
      <div class="identity">
        <p class="person-name">Idris Maren</p>
        <p class="person-role">General Manager</p>
      </div>
      <div class="divider"></div>
      <ul class="contacts">
        <li>
          <svg viewBox="0 0 16 16"><path d="M4 1.5l2.5 3-1.5 1.5a9 9 0 0 0 5 5l1.5-1.5 3 2.5-1.5 2.5C7 14.5 1.5 9 1.5 3z" fill="none" stroke="#c7ebf8" stroke-width="1.6"/></svg>
          043-555-0147
        </li>
        <li>
          <svg viewBox="0 0 16 16"><rect x="1" y="3" width="14" height="10" fill="#c7ebf8"/><path d="M1 3l7 6 7-6" fill="none" stroke="#0094d4" stroke-width="1.4"/></svg>
          hello@brindlesearch.com
        </li>
        <li>
          <svg viewBox="0 0 16 16"><path d="M8 1a4.5 4.5 0 0 0-4.5 4.5C3.5 9 8 14 8 14s4.5-5 4.5-8.5A4.5 4.5 0 0 0 8 1z" fill="#c7ebf8"/><circle cx="8" cy="5.5" r="1.6" fill="#0094d4"/></svg>
          <span>4210 Quarry Row Lane<br>Ashford, VA 20311</span>
        </li>
      </ul>
    </div>
    <div class="web-band">
      <svg viewBox="0 0 20 20"><g fill="none" stroke="#0094d4" stroke-width="1.4"><circle cx="10" cy="10" r="8.5"/><ellipse cx="10" cy="10" rx="3.8" ry="8.5"/><path d="M1.5 10h17M3 5.5h14M3 14.5h14"/></g></svg>
      www.brindlesearch.com
    </div>
  </section>

  <section class="card card-back">
    <div class="pattern-field" role="img" aria-label="Repeating brand pattern in soft blue tones"></div>
    <div class="back-mark"><span class="brand-dot"></span>Brindle Search</div>
  </section>
</body>
</html>
```